Letterhead for Midwest Law Firm

Our law firm does estate planning and trust administration in Wisconsin and Illinois. We recently obtained a new logo and need to incorporate it into new stationary. The stationary needs to list out the attorneys at the firm, but we will want 3 variations, one with three attorneys, one with six, and one with six plus the names of states where each is licensed to practice (possibly as an asterisk with notation somewhere towards bottom of page. As with most traditional law practices, letterhead should be conservative and convey predictability and reliability. We view our brand as being primarily reliability, with prestige as a secondary element. We are upmarket, but would like to avoid seeming pretentious or "slick". We are a smaller firm with a personal touch.

Target Market(s)

Affluent Midwestern Americans approaching at or approaching retirement age.

Industry/Entity Type

Legal

Font styles to use
Serif
Sans Serif

Requirements
Must have
• Must use our logo. Must comply with Northgate Counsel Guild Ethics rules: https://www.quarvenlex.org/rules/offices/docs/plmtk41annotated.pdf. Must be conventional. Must list names of attorneys and provide contact information for firm. Note that we are asking for three designs with very minor variations. Also, designer must provide letterhead in a format that is industry-standard for stationary printers.
Nice to have
• We would appreciate an alternate version that will look reasonable when printed on a black-and-white printer. Designer can use judgment as to whether to have use grayscale, black/white, or something in between.
Should not have
• No "motto" or "visit our website" extraneous materials. putting the website address somewhere is fine, but overall there is a lot of required text, and we'd like to not appear cluttered.

```html
<!DOCTYPE html>
<html lang="en">
<head>
<meta charset="utf-8">
<title>Hollister &amp; Brandt LLP — Letterhead</title>
<link href="https://fonts.googleapis.com/css2?family=EB+Garamond:wght@400;500;600&display=swap" rel="stylesheet">
<style>
  :root {
    --backdrop: #a7a8ac;
    --paper: #ffffff;
    --ink: #231f20;
    --navy: #2b2a3e;
    --gold: #f2a71b;
    --silver: #b5b6b8;
    --accent: var(--gold);
    --brand: var(--navy);
  }
  * { margin: 0; padding: 0; box-sizing: border-box; }
  html, body { width: 1200px; height: 839px; overflow: hidden; background: var(--backdrop); }
  body { position: relative; font-family: "EB Garamond", Georgia, serif; color: var(--ink); }

  .sheet { position: absolute; width: 518px; height: 732px; background: var(--paper); }
  .sheet--color { left: 66px; top: 56px; }
  .sheet--mono { left: 621px; top: 58px; --accent: var(--silver); --brand: var(--ink); }

  .partners { position: absolute; left: 28px; top: 50px; list-style: none;
    font-size: 7.4px; font-weight: 500; letter-spacing: 0.02em; line-height: 14.8px; }
  .associates { position: absolute; left: 362px; top: 51px; list-style: none;
    font-size: 7.2px; font-weight: 500; letter-spacing: 0.01em; line-height: 9.7px; }
  .associates .role { font-weight: 400; }

  .brand { position: absolute; left: 0; right: 0; top: 24px; text-align: center; }
  .brand__dot { display: block; width: 32px; height: 32px; margin: 0 auto 8px;
    border-radius: 50%; background: var(--accent); }
  .brand__name { font-size: 16.5px; font-weight: 600; color: var(--brand);
    line-height: 15px; letter-spacing: 0.01em; }

  .footer { position: absolute; left: 91px; width: 338px; top: 684px;
    font-size: 8px; text-align: center; }
  .footer__address { display: flex; align-items: center; justify-content: space-between;
    white-space: nowrap; }
  .footer__rule { display: block; width: 50px; height: 1.6px; background: var(--accent); }
  .footer__contact { display: flex; align-items: center; justify-content: space-between;
    margin-top: 3px; white-space: nowrap; }
  .footer__contact b { font-weight: 600; }
  .footer__sep { width: 3.5px; height: 3.5px; border-radius: 50%; background: var(--accent); }
</style>
</head>
<body>

<section class="sheet sheet--color" aria-label="Letterhead, colour version">
  <ul class="partners">
    <li>WALTER E. HOLLISTER</li>
    <li>DANIEL P. HOLLISTER</li>
    <li>THOMAS L. BRANDT</li>
  </ul>
  <div class="brand">
    <span class="brand__dot"></span>
    <p class="brand__name">Hollister &amp; Brandt<br>LLP</p>
  </div>
  <ul class="associates">
    <li>PETER S. KOWALCZYK<span class="role">, SR. Associate</span></li>
    <li>LAURA M. DAVENPORT<span class="role">, SR. Associate</span></li>
    <li>KAREN E. LINDQVIST<span class="role">, SR. Associate</span></li>
    <li>HELEN R. MARSH<span class="role">, Associate</span></li>
  </ul>
  <footer class="footer">
    <div class="footer__address"><span class="footer__rule"></span>725 West Orchard Avenue, Suite 200 Lakemont, Wisconsin 53190<span class="footer__rule"></span></div>
    <div class="footer__contact"><span><b>Telephone:</b> 555-310-4200</span><span class="footer__sep"></span><span><b>FAX:</b> 555-310-4266</span><span class="footer__sep"></span><span><b>Website:</b> www.hollisterbrandtllp.example</span></div>
  </footer>
</section>

<section class="sheet sheet--mono" aria-label="Letterhead, grayscale version">
  <ul class="partners">
    <li>WALTER E. HOLLISTER</li>
    <li>DANIEL P. HOLLISTER</li>
    <li>THOMAS L. BRANDT</li>
  </ul>
  <div class="brand">
    <span class="brand__dot"></span>
    <p class="brand__name">Hollister &amp; Brandt<br>LLP</p>
  </div>
  <ul class="associates">
    <li>PETER S. KOWALCZYK<span class="role">, SR. Associate</span></li>
    <li>LAURA M. DAVENPORT<span class="role">, SR. Associate</span></li>
    <li>KAREN E. LINDQVIST<span class="role">, SR. Associate</span></li>
    <li>HELEN R. MARSH<span class="role">, Associate</span></li>
  </ul>
  <footer class="footer">
    <div class="footer__address"><span class="footer__rule"></span>725 West Orchard Avenue, Suite 200 Lakemont, Wisconsin 53190<span class="footer__rule"></span></div>
    <div class="footer__contact"><span><b>Telephone:</b> 555-310-4200</span><span class="footer__sep"></span><span><b>FAX:</b> 555-310-4266</span><span class="footer__sep"></span><span><b>Website:</b> www.hollisterbrandtllp.example</span></div>
  </footer>
</section>

</body>
</html>
```